Logo and Flyer for Co-Branded Comedy Show

Graphic designer needed to create a promotional flyer for a comedy show. Two different comedy shows, with distinct branding, are joining forces to create a combined show. (co-branded logo to be included is attached.)

The design of the promotional materials should be a modern take on a vintage poster a la Quirkwood Jamboree. We'd like it to be a vintage look with a modern twist (I have attached the Quirkwood Jamboree Flyer for reference - marked up with info for our show) Filename: PLGRVN Flyer Mark Up

Images of the two hosts are attached: Filenames:

Our show will be in a theater, so if it can play off a playbill that would be great. I have attached examples of the clean look that we like, as well as some vintage theater flyers. We'd like to stay on the lighter side of the color palette (light gray, blues, etc. which is in line with the Harbor Laughs Live flyer) Filename: PLGR VN Flyer Direction

Current Branding of the individual Shows
I have attached the current promo materials for the individual shows, so you have a sense of the color palette and logo treatment.

The deliverable:
1 flyer vertical, 1 flyer horizontal - same design/concept but in 2 orientation (vertical and horizontal) horizontal will be used for web.
***This flyer will include the co-branded logo seen attached - Harbor Laughs Live Gets Real Honest (individual logos already created and attached) - Download PSD File here: http://lnk.example-short.test/PLGRVN

Industry/Entity Type

Graphic Designer

Colors
0493cd
85cae6
ecf7fb
f5f5f5
ffffff
606060
fbfbfb
0255a3
3176b5

Requirements
Must have
• Vintage look with a modern twist
• Vertical and horizontal options

```html
<!DOCTYPE html>
<html lang="en">
<head>
<meta charset="utf-8">
<title>Harbor Laughs Live – Gets Real Honest</title>
<link rel="stylesheet" href="https://fonts.googleapis.com/css2?family=Alfa+Slab+One&family=Arvo:wght@400;700&display=swap">
<style>
  :root {
    --stage: #e6e6e6;
    --paper: #f4efe4;
    --paper-edge: #e9dfcb;
    --blue-deep: #0255a3;
    --blue-mid: #3176b5;
    --blue-light: #6f9fd2;
    --ink-gray: #606060;
    --frame: #3a3a3a;
    --frame-ring: #d8d8d8;
  }
  * { box-sizing: border-box; margin: 0; padding: 0; }
  html, body { width: 1200px; height: 900px; overflow: hidden; }
  body {
    background: var(--stage);
    display: flex; align-items: center; justify-content: center; gap: 24px;
    font-family: "Arvo", serif;
  }

  /* shared flyer pieces */
  .flyer {
    background: radial-gradient(ellipse at center, var(--paper) 55%, var(--paper-edge) 100%);
    box-shadow: 0 6px 22px rgba(0,0,0,.18);
    display: flex; flex-direction: column; align-items: center;
    text-align: center;
  }
  .rule { width: 100%; border-top: 3px solid var(--blue-mid); border-bottom: 1px solid var(--blue-mid); height: 6px; flex: none; }
  .date-line {
    width: 100%; display: flex; justify-content: space-between;
    font-family: "Alfa Slab One", serif; color: var(--blue-mid);
    letter-spacing: 2px; padding: 4px 2px;
  }
  .presenter { font-family: "Alfa Slab One", serif; color: var(--blue-deep); }
  .presenter span { color: var(--ink-gray); letter-spacing: 2px; margin-left: 5px; font-size: .75em; }
  .show-logo { font-family: "Alfa Slab One", serif; color: var(--blue-mid); line-height: 1.05; font-weight: 400; }
  .show-logo .primary, .show-logo .secondary { display: block; }
  .show-type {
    color: var(--ink-gray); letter-spacing: 3px;
    display: flex; align-items: center; gap: 10px; width: 100%;
  }
  .show-type::before, .show-type::after { content: ""; flex: 1; border-top: 2px solid var(--blue-mid); }
  .hosted-by { font-family: "Alfa Slab One", serif; color: var(--blue-deep); letter-spacing: 2px; font-weight: 400; line-height: 1.1; }
  .host-name { font-family: "Alfa Slab One", serif; color: var(--blue-light); letter-spacing: 1px; white-space: nowrap; }
  .portrait {
    border-radius: 50%; flex: none;
    border: 12px solid var(--frame);
    box-shadow: inset 0 0 0 3px var(--frame-ring), 0 3px 8px rgba(0,0,0,.3);
  }
  .portrait--zolo { background: radial-gradient(circle at 50% 45%, #b08a74, #3b2b28 70%, #1e1e1e); }
  .portrait--marla { background: radial-gradient(circle at 50% 45%, #6b4a3a, #1f1a18 65%, #2f6f67); }
  .featuring { font-family: "Alfa Slab One", serif; color: var(--ink-gray); letter-spacing: 3px; }
  .lineup { font-family: "Alfa Slab One", serif; color: var(--blue-mid); line-height: 1.5; white-space: nowrap; }
  .venue { color: var(--ink-gray); font-weight: 700; letter-spacing: 5px; }
  .address { color: var(--ink-gray); }
  .site { font-family: "Alfa Slab One", serif; color: var(--blue-mid); letter-spacing: 5px; }
  .rule--bottom { margin-top: auto; }

  /* vertical flyer */
  .flyer--vertical { width: 470px; height: 660px; padding: 16px 22px; }
  .flyer--vertical .date-line { font-size: 13px; }
  .flyer--vertical .presenter { font-size: 13px; margin-top: 8px; }
  .flyer--vertical .show-logo { margin-top: 8px; }
  .flyer--vertical .show-logo .primary { font-size: 34px; }
  .flyer--vertical .show-logo .secondary { font-size: 22px; }
  .flyer--vertical .show-type { font-size: 16px; margin-top: 10px; }
  .flyer--vertical .hosted-by { font-size: 30px; margin-top: 2px; }
  .flyer--vertical .host-row { width: 100%; display: flex; justify-content: space-between; padding: 0 30px; font-size: 14px; }
  .flyer--vertical .hosts { width: 100%; display: flex; justify-content: center; gap: 18px; margin-top: 8px; height: 200px; }
  .flyer--vertical .portrait { width: 160px; height: 190px; }
  .flyer--vertical .portrait--zolo { margin-top: 10px; }
  .flyer--vertical .featuring { font-size: 15px; margin-top: 8px; }
  .flyer--vertical .lineup { font-size: 11px; margin-top: 2px; }
  .flyer--vertical .venue { font-size: 12px; margin-top: 6px; }
  .flyer--vertical .address { font-size: 11px; }
  .flyer--vertical .site { font-size: 14px; margin-top: 4px; }

  /* horizontal flyer */
  .flyer--horizontal { width: 680px; height: 480px; padding: 14px 20px; }
  .flyer--horizontal .date-line { font-size: 13px; }
  .flyer--horizontal .body-grid {
    width: 100%; flex: 1; display: grid; grid-template-columns: 150px 1fr 150px; gap: 10px; align-items: center;
  }
  .flyer--horizontal .host-col { display: flex; flex-direction: column; align-items: center; gap: 10px; }
  .flyer--horizontal .portrait { width: 140px; height: 170px; }
  .flyer--horizontal .host-name { font-size: 12px; }
  .flyer--horizontal .center-col { display: flex; flex-direction: column; align-items: center; }
  .flyer--horizontal .presenter { font-size: 12px; }
  .flyer--horizontal .show-logo { margin-top: 6px; }
  .flyer--horizontal .show-logo .primary { font-size: 26px; }
  .flyer--horizontal .show-logo .secondary { font-size: 18px; }
  .flyer--horizontal .show-type { font-size: 13px; margin-top: 8px; }
  .flyer--horizontal .hosted-by { font-size: 24px; }
  .flyer--horizontal .featuring { font-size: 13px; margin-top: 8px; }
  .flyer--horizontal .lineup { font-size: 12px; margin-top: 2px; }
  .flyer--horizontal .venue { font-size: 11px; margin-top: 6px; }
  .flyer--horizontal .address { font-size: 10px; }
  .flyer--horizontal .site { font-size: 13px; margin-top: 4px; }
</style>
</head>
<body>
  <main class="flyer flyer--vertical">
    <div class="rule"></div>
    <div class="date-line"><span>ONE NIGHT</span><span>SATURDAY</span><span>AUGUST 22, 2015</span></div>
    <div class="rule"></div>
    <p class="presenter">Pale Birch Productions<span>PRESENTS</span></p>
    <h1 class="show-logo">
      <span class="primary">Harbor Laughs Live</span>
      <span class="secondary">Gets Real Honest</span>
    </h1>
    <p class="show-type">COMEDY &amp; SHOW</p>
    <h2 class="hosted-by">HOSTED BY</h2>
    <div class="host-row"><span class="host-name">ZOLO BRIGHTWAVE</span><span class="host-name">MARLA VINTROW</span></div>
    <div class="hosts">
      <div class="portrait portrait--zolo" role="img" aria-label="Portrait photo of host Zolo Brightwave"></div>
      <div class="portrait portrait--marla" role="img" aria-label="Portrait photo of host Marla Vintrow"></div>
    </div>
    <p class="featuring">FEATURING</p>
    <p class="lineup">DELL FARROW * OWEN PRICKLET * TAMSIN ROE<br>GUS HALLERT * IVY MARCHETTI * RUDY OKAFOR &amp; more</p>
    <p class="venue">LARKSPUR THEATER</p>
    <p class="address">48 TIDEWELL AVE HARBORVIEW, NY 10999</p>
    <p class="site">PLGRVN.COM</p>
    <div class="rule rule--bottom"></div>
  </main>

  <section class="flyer flyer--horizontal">
    <div class="rule"></div>
    <div class="date-line"><span>ONE NIGHT</span><span>SATURDAY</span><span>AUGUST 22, 2015</span></div>
    <div class="rule"></div>
    <div class="body-grid">
      <div class="host-col">
        <div class="portrait portrait--zolo" role="img" aria-label="Portrait photo of host Zolo Brightwave"></div>
        <span class="host-name">ZOLO BRIGHTWAVE</span>
      </div>
      <div class="center-col">
        <p class="presenter">Pale Birch Productions<span>PRESENTS</span></p>
        <h2 class="show-logo">
          <span class="primary">Harbor Laughs Live</span>
          <span class="secondary">Gets Real Honest</span>
        </h2>
        <p class="show-type">COMEDY &amp; SHOW</p>
        <p class="hosted-by">HOSTED BY</p>
        <p class="featuring">FEATURING</p>
        <p class="lineup">DELL FARROW * OWEN PRICKLET<br>TAMSIN ROE * GUS HALLERT<br>IVY MARCHETTI * RUDY OKAFOR &amp; more</p>
        <p class="venue">LARKSPUR THEATER</p>
        <p class="address">48 TIDEWELL AVE HARBORVIEW, NY 10999</p>
        <p class="site">PLGRVN.COM</p>
      </div>
      <div class="host-col">
        <div class="portrait portrait--marla" role="img" aria-label="Portrait photo of host Marla Vintrow"></div>
        <span class="host-name">MARLA VINTROW</span>
      </div>
    </div>
    <div class="rule"></div>
  </section>
</body>
</html>
```